Business Card & Stationary
For Event Planning Website
I need single sided standard sized Business Card [3.5" x 2"]
Same as logo or similar
Professional
First Name Last Name
Founder & Chief Executive Officer
Address 1
Address 2
New York, NY 10016
xyz@juniperhours.com
www.juniperhours.com
Feel free to be creative - the site is for party planning (weddings, bar-mitzvahs, etc.) so it should be modern & professional, with a fun factor.
I used test data to protect personal data but I can supply you with all of the information you need later.
I'm not sure which eps file corresponds to the jpg.
This is the hamsa (hand) which is part of the logo
The hand - ai file
Webpage Background Pattern

```html
<!DOCTYPE html>
<html lang="en">
<head>
<meta charset="utf-8">
<title>JuniperHours Stationery</title>
<link href="https://fonts.googleapis.com/css2?family=Ubuntu:wght@400&family=Open+Sans:wght@400;600&display=swap" rel="stylesheet">
<style>
  :root {
    --backdrop: #ebebeb;
    --paper: #ffffff;
    --brand: #1587d6;
    --brand-deep: #0b6fc0;
    --brand-light: #8fd6f7;
    --ink: #4a5560;
    --ghost: #e6eef7;
    --shadow: rgba(0,0,0,0.18);
  }
  * { box-sizing: border-box; margin: 0; padding: 0; }
  html, body { width: 1200px; height: 881px; overflow: hidden; }
  body { background: var(--backdrop); position: relative; font-family: "Open Sans", Arial, sans-serif; color: var(--ink); }

  .sheet { position: absolute; background: var(--paper); box-shadow: 0 1px 4px var(--shadow); overflow: hidden; }
  .wordmark { position: absolute; font-family: "Ubuntu", Arial, sans-serif; font-weight: 400; color: var(--brand); white-space: nowrap; letter-spacing: -0.3px; }
  .mark-dot { position: absolute; border-radius: 50%; border: 2px solid var(--brand); }
  .band { position: absolute; height: 14px; background: linear-gradient(90deg, var(--brand-deep), var(--brand) 55%, var(--brand-light)); }
  .band-line { position: absolute; height: 2px; background: var(--brand); opacity: .7; }
  .emblem-area { position: absolute; background: var(--ghost); border-radius: 46% 46% 40% 40%; }
  .fine { position: absolute; font-size: 6px; line-height: 8px; white-space: nowrap; }

  /* Letterhead */
  .letterhead { left: 29px; top: 31px; width: 518px; height: 814px; }
  .letterhead .wordmark { right: 12px; top: 10px; font-size: 25px; }
  .letterhead .band { left: 12px; right: 12px; top: 46px; }
  .letterhead .band-line { left: 12px; right: 12px; top: 64px; }
  .letterhead .mark-dot { right: 14px; top: 72px; width: 12px; height: 12px; }
  .letterhead .emblem-area { left: 310px; top: 520px; width: 230px; height: 300px; }
  .letterhead .footer { left: 0; right: 0; bottom: 8px; text-align: center; }

  /* Business card */
  .card { left: 595px; top: 31px; width: 221px; height: 125px; border-radius: 10px; }
  .card .wordmark { right: 8px; top: 4px; font-size: 16px; }
  .card .band { left: 6px; right: 6px; top: 26px; height: 11px; }
  .card .name { position: absolute; left: 10px; top: 27px; font-size: 7px; color: #fff; font-weight: 600; }
  .card .band-line { left: 6px; right: 6px; top: 39px; height: 1px; }
  .card .title { left: 10px; top: 42px; }
  .card .mark-dot { right: 9px; top: 42px; width: 9px; height: 9px; border-width: 1.5px; }
  .card .address { left: 10px; top: 62px; }
  .card .contact { right: 10px; top: 62px; text-align: right; }

  /* Envelope front */
  .envelope { left: 595px; top: 211px; width: 576px; height: 298px; }
  .envelope .wordmark { right: 14px; top: 8px; font-size: 24px; }
  .envelope .band { left: 12px; right: 12px; top: 42px; height: 10px; }
  .envelope .band-line { left: 12px; right: 12px; top: 56px; }
  .envelope .mark-dot { right: 18px; top: 62px; width: 11px; height: 11px; }
  .envelope .emblem-area { left: 390px; top: 90px; width: 150px; height: 198px; }
  .envelope .return { left: 12px; bottom: 20px; }

  /* Envelope back */
  .envelope-back { left: 595px; top: 552px; width: 576px; height: 300px; }
  .flap { position: absolute; left: 0; top: 0; width: 576px; height: 110px; }
  .envelope-back .wordmark { left: 0; right: 0; top: 18px; text-align: center; font-size: 25px; color: #fff; }
  .envelope-back .mark-dot { left: 282px; top: 54px; width: 12px; height: 12px; border-color: #fff; }
</style>
</head>
<body>

<section class="sheet letterhead" aria-label="Letterhead">
  <div class="wordmark">JuniperHours</div>
  <div class="band"></div>
  <div class="band-line"></div>
  <div class="mark-dot"></div>
  <div class="emblem-area" role="img" aria-label="Faint hand emblem decoration"></div>
  <div class="fine footer">
    Address 1 | Address 2<br>
    New York, NY 10016<br>
    Phone: (212) 555-0148 | Email: xyz@juniperhours.com | www.juniperhours.com
  </div>
</section>

<section class="sheet card" aria-label="Business card">
  <div class="wordmark">JuniperHours</div>
  <div class="band"></div>
  <div class="name">First Name Last Name</div>
  <div class="band-line"></div>
  <div class="fine title">Founder &amp; Chief Executive Officer</div>
  <div class="mark-dot"></div>
  <div class="fine address">Address 1<br>Address 2<br>New York, NY 10016</div>
  <div class="fine contact">Phone (212) 555-0148<br>Email xyz@juniperhours.com<br>www.juniperhours.com</div>
</section>

<section class="sheet envelope" aria-label="Envelope front">
  <div class="wordmark">JuniperHours</div>
  <div class="band"></div>
  <div class="band-line"></div>
  <div class="mark-dot"></div>
  <div class="emblem-area" role="img" aria-label="Faint hand emblem decoration"></div>
  <div class="fine return">Address 1<br>Address 2<br>New York, NY 10016<br>Phone (212) 555-0148 | Email: xyz@juniperhours.com | www.juniperhours.com</div>
</section>

<section class="sheet envelope-back" aria-label="Envelope back">
  <svg class="flap" viewBox="0 0 576 110" aria-hidden="true">
    <defs>
      <linearGradient id="flapFill" x1="0" x2="1" y1="0" y2="0">
        <stop offset="0" stop-color="#0b6fc0"/>
        <stop offset="0.5" stop-color="#3fb0ec"/>
        <stop offset="1" stop-color="#0b6fc0"/>
      </linearGradient>
    </defs>
    <path d="M0 0 H576 V80 Q288 110 0 80 Z" fill="url(#flapFill)"/>
  </svg>
  <div class="wordmark">JuniperHours</div>
  <div class="mark-dot"></div>
</section>

</body>
</html>
```